Biz cards and stationary for high tech company
DALMIX Technology
I need single sided standard sized Business Card [3.5" x 2"]
either from logo or standard
Professional
First Last
Title
address
city, state, zip
800.XXX.XXXX
XXX.XXX.XXXX
sales@dalmixtek.example
www.dalmixtek.example
- one or 2-sided cards ok

```html
<!DOCTYPE html>
<html lang="en">
<head>
<meta charset="utf-8">
<title>DALMIX Technology – Business Card</title>
<link href="https://fonts.googleapis.com/css2?family=Exo+2:wght@400;600;800&display=swap" rel="stylesheet">
<style>
  :root {
    --bg: #e4e6e8;
    --card: #ffffff;
    --blue: #1f73c6;
    --blue-deep: #0f4f98;
    --grey-swoosh: #c9ccd0;
    --ink: #6f757c;
    --ink-soft: #9aa0a6;
  }
  html, body {
    margin: 0;
    width: 1200px;
    height: 984px;
    overflow: hidden;
    background: var(--bg);
    font-family: "Exo 2", sans-serif;
  }
  .stage {
    width: 1200px;
    height: 984px;
    display: flex;
    flex-direction: column;
    align-items: center;
    justify-content: center;
    gap: 34px;
  }
  .card {
    position: relative;
    width: 780px;
    height: 446px;
    background: var(--card);
    border-radius: 22px;
    overflow: hidden;
    box-shadow: 0 6px 18px rgba(0,0,0,.12);
  }
  .card-art { position: absolute; inset: 0; }

  /* back side */
  .back-brand {
    position: absolute;
    left: 0; right: 0; top: 150px;
    display: flex; align-items: center; justify-content: center; gap: 14px;
  }
  .brand-dot {
    width: 56px; height: 56px; border-radius: 50%;
    background: var(--blue);
  }
  .brand-name {
    font-weight: 800;
    color: var(--blue);
    letter-spacing: 2px;
  }
  .back-brand .brand-name { font-size: 40px; }
  .back-web {
    position: absolute;
    left: 0; right: 0; top: 300px;
    text-align: center;
    font-size: 13px;
    letter-spacing: 6px;
    color: var(--ink-soft);
    text-transform: uppercase;
  }

  /* front side */
  .front-brand {
    position: absolute; left: 44px; top: 96px;
  }
  .front-brand .row { display: flex; align-items: center; gap: 14px; }
  .front-brand .brand-dot { width: 60px; height: 60px; }
  .front-brand .brand-name { font-size: 50px; }
  .tagline {
    margin: 2px 0 0 76px;
    font-size: 14px;
    letter-spacing: 3px;
    color: var(--ink);
    text-transform: uppercase;
  }
  .person {
    position: absolute; left: 44px; top: 296px;
    text-transform: uppercase;
    letter-spacing: 4px;
  }
  .person-name { color: var(--blue); font-size: 17px; font-weight: 600; }
  .person-title { color: var(--ink); font-size: 14px; margin-top: 6px; }

  .contact {
    position: absolute; left: 482px; top: 300px;
    margin: 0; padding: 0; list-style: none;
    font-size: 12.5px;
    letter-spacing: 1.5px;
    color: var(--ink);
    text-transform: uppercase;
    line-height: 17px;
  }
  .contact li { display: flex; align-items: flex-start; gap: 8px; }
  .contact .lower { text-transform: none; }
  .contact-icon {
    flex: none; width: 11px; height: 11px; margin-top: 3px;
    border-radius: 50%; background: var(--blue);
  }
  .contact-icon.blank { background: none; }
</style>
</head>
<body>
<main class="stage">

  <section class="card card-back" aria-label="Card back">
    <div class="back-brand">
      <span class="brand-dot"></span>
      <span class="brand-name">DALMIX</span>
    </div>
    <div class="back-web">www.dalmixtek.example</div>
  </section>

  <section class="card card-front" aria-label="Card front">
    <svg class="card-art" viewBox="0 0 780 446" preserveAspectRatio="none" aria-hidden="true">
      <path d="M0 0 H780 V20 C560 8 320 30 0 58 Z" fill="var(--blue)"/>
      <path d="M0 58 C320 30 560 8 780 20 V446 H700 C720 330 640 180 420 112 C300 78 150 66 0 70 Z" fill="var(--blue)"/>
      <path d="M0 70 C150 66 300 78 420 112 C640 180 720 330 700 446 H686 C700 330 620 196 410 128 C290 92 150 80 0 82 Z" fill="var(--grey-swoosh)"/>
      <path d="M0 82 C150 80 290 92 410 128 C620 196 700 330 686 446 H682 C694 332 612 202 404 136 C288 100 150 88 0 90 Z" fill="#ffffff"/>
      <path d="M780 20 V446 H720 C748 300 690 150 520 70 C640 40 720 26 780 20 Z" fill="var(--blue-deep)" opacity=".35"/>
    </svg>

    <div class="front-brand">
      <div class="row">
        <span class="brand-dot"></span>
        <span class="brand-name">DALMIX</span>
      </div>
      <div class="tagline">Technology Corporation</div>
    </div>

    <div class="person">
      <div class="person-name">Harlow</div>
      <div class="person-title">CEO</div>
    </div>

    <ul class="contact">
      <li><span class="contact-icon"></span><span>1450 Alder St.</span></li>
      <li><span class="contact-icon blank"></span><span>Brookfield, OR 97010</span></li>
      <li><span class="contact-icon"></span><span>800.555.0142</span></li>
      <li><span class="contact-icon"></span><span>503.555.0187</span></li>
      <li><span class="contact-icon"></span><span>503.555.0193</span></li>
      <li><span class="contact-icon"></span><span class="lower">sales@dalmixtek.example</span></li>
      <li><span class="contact-icon"></span><span class="lower">www.dalmixtek.example</span></li>
    </ul>
  </section>

</main>
</body>
</html>
```